Marketing Flyer for churches and schools

We need a marketing flyer design for ongoing marketing activities. We are a bounce house and inflatable slide rental company. This flyer would be sent to churches schools and other non profits. We would like to create a set background for our flyer and then be able to edit the body of the text as we see fit. This will allow us to use this design for marketing throughout the year.

Target Market(s)

Schools and Churches

Requirements
Must have
• create flyer background with editable text fields that we can modify as we see fit. Should fit on letter size paper.
Nice to have
• A brochure style option along with the flyer.
Should not have
• N/A

```html
<!DOCTYPE html>
<html lang="en">
<head>
<meta charset="utf-8">
<title>Hop Harbor Rentals – Flyer</title>
<link href="https://fonts.googleapis.com/css2?family=Quicksand:wght@700&family=Source+Sans+3:wght@400;600&display=swap" rel="stylesheet">
<style>
  :root {
    --stage: #e4e1dc;
    --paper: #f2f2f2;
    --orange: #f7941d;
    --orange-deep: #f15a29;
    --ink: #4a4a4a;
    --white: #ffffff;
    --slide-green: #2f8a6a;
    --slide-red: #d9463a;
    --slide-yellow: #f2c94c;
  }
  * { box-sizing: border-box; margin: 0; padding: 0; }
  html, body {
    width: 976px; height: 1200px; overflow: hidden;
    background: var(--stage);
  }
  .flyer {
    position: absolute; left: 269px; top: 92px;
    width: 438px; height: 1015px;
    background: var(--paper);
    box-shadow: 0 4px 14px rgba(0,0,0,.18);
    overflow: hidden;
  }
  .brand {
    position: absolute; left: 0; top: 40px; width: 100%; height: 310px;
    display: flex; flex-direction: column; align-items: center; justify-content: center; gap: 18px;
  }
  .brand-dot {
    width: 56px; height: 56px; border-radius: 50%;
    background: var(--orange);
  }
  .brand-name {
    font-family: "Quicksand", sans-serif; font-weight: 700;
    font-size: 62px; line-height: 1.05; text-align: center;
    color: var(--orange);
  }
  .swoosh { position: absolute; left: 0; width: 438px; }
  .swoosh-top { top: 372px; height: 128px; }
  .swoosh-bottom { top: 893px; height: 122px; }
  .headline {
    position: absolute; left: 20px; right: 20px; top: 505px;
    font-family: "Quicksand", sans-serif; font-weight: 700;
    font-size: 17px; line-height: 22px; text-align: center;
    color: var(--orange-deep); letter-spacing: .3px;
  }
  .body-copy {
    position: absolute; left: 30px; right: 30px; top: 606px;
    font-family: "Source Sans 3", sans-serif; font-size: 12.5px;
    line-height: 1.35; text-align: center; color: var(--ink);
  }
  .body-copy p + p { margin-top: 14px; }
  .product-photo {
    position: absolute; left: 68px; top: 732px; width: 298px; height: 158px;
    border-radius: 20px 40px 10px 10px;
    background: linear-gradient(100deg, var(--slide-green) 0%, var(--slide-yellow) 40%, var(--slide-red) 75%, #e0833a 100%);
    opacity: .85;
  }
  .contact {
    position: absolute; left: 0; right: 0; top: 958px;
    font-family: "Source Sans 3", sans-serif; font-weight: 600;
    font-size: 13.5px; line-height: 1.3; text-align: center; color: var(--white);
  }
  .contact-line { display: flex; justify-content: center; align-items: center; gap: 5px; }
  .icon { width: 12px; height: 12px; }
</style>
</head>
<body>
  <main class="flyer">
    <div class="brand">
      <span class="brand-dot"></span>
      <span class="brand-name">Hop Harbor<br>Rentals</span>
    </div>

    <svg class="swoosh swoosh-top" viewBox="0 0 438 128" preserveAspectRatio="none" aria-hidden="true">
      <defs>
        <linearGradient id="band" x1="0" x2="1">
          <stop offset="0" stop-color="#f7941d"/>
          <stop offset="1" stop-color="#f15a29"/>
        </linearGradient>
        <linearGradient id="shade" x1="0" y1="0" x2="0" y2="1">
          <stop offset="0" stop-color="#000" stop-opacity=".2"/>
          <stop offset="1" stop-color="#000" stop-opacity="0"/>
        </linearGradient>
      </defs>
      <path d="M0 0 H438 V48 C300 40 150 50 0 70 Z" fill="url(#band)"/>
      <path d="M0 100 C150 65 300 54 438 53 V62 C300 64 150 90 0 128 Z" fill="url(#band)"/>
      <path d="M0 128 C150 90 300 64 438 62 V78 C300 76 150 100 0 128 Z" fill="url(#shade)"/>
    </svg>

    <h1 class="headline">Backyard parties to community events,<br>we have the inflatable units you need<br>to ensure fun for all.</h1>

    <div class="body-copy">
      <p>Inflatable rentals from Hop Harbor Rentals are the centerpiece attraction for birthday parties and family gatherings and a great addition to school, church, and community events.</p>
      <p>Bounce houses are family-friendly fun that keeps children entertained for hours. Give us a call or reserve online today.</p>
    </div>

    <div class="product-photo" role="img" aria-label="Photo of an inflatable castle bounce house with attached slide"></div>

    <svg class="swoosh swoosh-bottom" viewBox="0 0 438 122" preserveAspectRatio="none" aria-hidden="true">
      <path d="M0 44 C150 20 300 8 438 2 V12 C300 16 150 28 0 52 Z" fill="url(#band)"/>
      <path d="M0 62 C150 40 300 28 438 24 V122 H0 Z" fill="url(#band)"/>
    </svg>

    <div class="contact">
      <div>For more information email us or call</div>
      <div class="contact-line">
        <svg class="icon" viewBox="0 0 16 16" aria-hidden="true"><rect x="1" y="3" width="14" height="10" rx="1.5" fill="var(--slide-yellow)"/><path d="M1.5 4 L8 9 L14.5 4" stroke="var(--orange-deep)" stroke-width="1.3" fill="none"/></svg>
        <span>info@hopharborrentals.com or</span>
        <svg class="icon" viewBox="0 0 16 16" aria-hidden="true"><path d="M4 1.5 L6.5 4.5 L5 6.5 C6 8.5 7.5 10 9.5 11 L11.5 9.5 L14.5 12 L13 14.5 C7 14.5 1.5 9 1.5 3 Z" fill="var(--slide-yellow)"/></svg>
        <span>555-010-2468</span>
      </div>
    </div>
  </main>
</body>
</html>
```